business card, letterhead, and envelope design for mobile ultrasound imaging
Corvane Sonography Partners, LLC
Simple
Maren Tocks BS, RDMS, RVT
Managing Partner
6184 County Road 41S
Calloway Reach, FL 39041
P.O. Box 7126
Tessaly Point, FL 39052-5453
marentocks@corvanesono.example
www.corvanesono.example

```html
<!DOCTYPE html>
<html lang="en">
<head>
<meta charset="utf-8">
<title>Corvane Sonography Partners — Stationery Concepts</title>
<link rel="stylesheet" href="https://fonts.googleapis.com/css2?family=Cinzel:wght@600&family=Open+Sans:wght@400;600&display=swap">
<style>
  :root {
    --board: #3b3b3c;
    --board-dark: #2c2c2d;
    --paper: #ffffff;
    --paper-shade: #eef0f1;
    --blue: #1b9fd9;
    --green: #8cc63f;
    --ink: #1f6f9c;
    --grey-text: #6b6f73;
    --caption: #9a9a9a;
  }
  * { margin: 0; padding: 0; box-sizing: border-box; }
  html, body { width: 1200px; height: 446px; overflow: hidden; }
  body {
    background: radial-gradient(ellipse at 50% 40%, var(--board) 0%, var(--board-dark) 100%);
    font-family: "Open Sans", Arial, sans-serif;
    position: relative;
  }
  .piece { position: absolute; box-shadow: 0 3px 8px rgba(0,0,0,.45); background: var(--paper); overflow: hidden; }
  .piece svg { display: block; width: 100%; height: 100%; }
  .caption { position: absolute; font-size: 7px; color: var(--caption); text-align: center; }
  .brand-name { font-family: "Cinzel", Georgia, serif; font-weight: 600; fill: var(--ink); }
  .contact { font-family: "Open Sans", Arial, sans-serif; fill: var(--grey-text); }

  .title-block { position: absolute; left: 30px; top: 108px; width: 150px; text-align: center; }
  .title-block .mark { width: 30px; height: 30px; border-radius: 50%; background: var(--blue); margin: 0 auto 8px; }
  .title-block .name { font-family: "Cinzel", Georgia, serif; font-weight: 600; color: var(--paper); font-size: 10px; line-height: 1.25; }
  .title-block .sub { font-size: 7px; color: var(--caption); margin-top: 5px; }

  .card-front { left: 22px; top: 212px; width: 168px; height: 92px; }
  .card-back { left: 22px; top: 318px; width: 168px; height: 92px; }
  .letterhead-one { left: 199px; top: 18px; width: 282px; height: 382px; }
  .letterhead-two { left: 504px; top: 18px; width: 282px; height: 382px; }
  .envelope-green { left: 826px; top: 44px; width: 350px; height: 92px; }
  .envelope-blue { left: 826px; top: 144px; width: 350px; height: 92px; }
  .envelope-front-a { left: 836px; top: 244px; width: 340px; height: 76px; }
  .envelope-front-b { left: 826px; top: 326px; width: 350px; height: 78px; }
</style>
</head>
<body>

<div class="title-block">
  <div class="mark"></div>
  <div class="name">Corvane Sonography Partners, LLC</div>
  <div class="sub">Stationery Concepts</div>
</div>

<div class="piece card-front">
  <svg viewBox="0 0 168 92">
    <text class="contact" x="158" y="15" font-size="5" text-anchor="end" font-weight="600">Maren Tocks BS, RDMS, RVT</text>
    <text class="contact" x="158" y="21" font-size="4" text-anchor="end">Managing Partner</text>
    <text class="contact" x="158" y="33" font-size="3.6" text-anchor="end">6184 County Road 41S</text>
    <text class="contact" x="158" y="38" font-size="3.6" text-anchor="end">Calloway Reach, FL 39041</text>
    <text class="contact" x="158" y="43" font-size="3.6" text-anchor="end">P.O. Box 7126, Tessaly Point, FL 39052-7126</text>
    <text class="contact" x="158" y="48" font-size="3.6" text-anchor="end">marentocks@corvanesono.example</text>
    <text class="contact" x="158" y="53" font-size="3.6" text-anchor="end">www.corvanesono.example</text>
    <path d="M0 68 C40 60 95 80 168 64 L168 92 L0 92 Z" fill="var(--green)"/>
    <path d="M0 74 C45 66 100 86 168 70 L168 92 L0 92 Z" fill="var(--blue)"/>
  </svg>
</div>
<div class="caption" style="left:22px;top:306px;width:168px;">Front side</div>

<div class="piece card-back">
  <svg viewBox="0 0 168 92">
    <circle cx="40" cy="36" r="7" fill="var(--blue)"/>
    <text class="brand-name" x="52" y="34" font-size="6">Corvane Sonography</text>
    <text class="brand-name" x="52" y="42" font-size="6">Partners, LLC</text>
    <path d="M0 70 C45 62 100 82 168 66 L168 92 L0 92 Z" fill="var(--green)"/>
    <path d="M0 76 C45 68 100 88 168 72 L168 92 L0 92 Z" fill="var(--blue)"/>
  </svg>
</div>
<div class="caption" style="left:22px;top:412px;width:168px;">Back side</div>

<div class="piece letterhead-one">
  <svg viewBox="0 0 282 382">
    <circle cx="28" cy="22" r="6" fill="var(--blue)"/>
    <text class="brand-name" x="38" y="20" font-size="5.5">Corvane Sonography</text>
    <text class="brand-name" x="38" y="27" font-size="5.5">Partners, LLC</text>
    <text class="contact" x="146" y="16" font-size="3.6">6184 County Road 41S</text>
    <text class="contact" x="146" y="21" font-size="3.6">Calloway Reach, FL 39041</text>
    <text class="contact" x="146" y="26" font-size="3.6">P.O. Box 7126</text>
    <text class="contact" x="146" y="31" font-size="3.6">Tessaly Point, FL 39052-7126</text>
    <path d="M0 350 C80 334 165 366 282 340 L282 382 L0 382 Z" fill="var(--green)"/>
    <path d="M0 358 C80 342 165 374 282 348 L282 382 L0 382 Z" fill="var(--blue)"/>
  </svg>
</div>
<div class="caption" style="left:199px;top:406px;width:282px;">Letterhead option #1</div>

<div class="piece letterhead-two">
  <svg viewBox="0 0 282 382">
    <circle cx="28" cy="22" r="6" fill="var(--blue)"/>
    <text class="brand-name" x="38" y="20" font-size="5.5">Corvane Sonography</text>
    <text class="brand-name" x="38" y="27" font-size="5.5">Partners, LLC</text>
    <path d="M0 342 C90 326 172 360 282 334 L282 382 L0 382 Z" fill="var(--green)"/>
    <path d="M0 350 C90 334 172 368 282 342 L282 382 L0 382 Z" fill="var(--blue)"/>
    <text x="141" y="366" font-size="3.4" text-anchor="middle" fill="#ffffff">6184 County Road 41S, Calloway Reach, FL 39041 • P.O. Box 7126, Tessaly Point, FL 39052-7126</text>
    <text x="141" y="372" font-size="3.4" text-anchor="middle" fill="#ffffff">marentocks@corvanesono.example • www.corvanesono.example</text>
  </svg>
</div>
<div class="caption" style="left:504px;top:406px;width:282px;">Letterhead option #2</div>

<div class="piece envelope-green">
  <svg viewBox="0 0 350 92">
    <rect width="350" height="92" fill="var(--paper-shade)"/>
    <path d="M0 0 L350 0 L350 20 L175 56 L0 20 Z" fill="var(--green)"/>
    <circle cx="175" cy="30" r="6" fill="#ffffff"/>
  </svg>
</div>

<div class="piece envelope-blue">
  <svg viewBox="0 0 350 92">
    <rect width="350" height="92" fill="var(--paper-shade)"/>
    <path d="M0 0 L350 0 L350 20 L175 56 L0 20 Z" fill="var(--blue)"/>
    <circle cx="175" cy="30" r="6" fill="#ffffff"/>
  </svg>
</div>

<div class="piece envelope-front-a">
  <svg viewBox="0 0 340 76">
    <path d="M0 0 L340 0 L170 36 Z" fill="var(--paper-shade)"/>
    <circle cx="170" cy="22" r="5" fill="var(--blue)"/>
    <path d="M0 62 C110 52 215 72 340 56 L340 76 L0 76 Z" fill="var(--green)"/>
    <path d="M0 67 C110 57 215 77 340 61 L340 76 L0 76 Z" fill="var(--blue)"/>
  </svg>
</div>

<div class="piece envelope-front-b">
  <svg viewBox="0 0 350 78">
    <circle cx="18" cy="12" r="5" fill="var(--blue)"/>
    <text class="brand-name" x="27" y="11" font-size="5">Corvane Sonography</text>
    <text class="brand-name" x="27" y="17" font-size="5">Partners, LLC</text>
    <text class="contact" x="27" y="24" font-size="3.4">6184 County Road 41S</text>
    <text class="contact" x="27" y="28" font-size="3.4">Calloway Reach, FL 39041</text>
    <path d="M0 64 C110 54 225 74 350 58 L350 78 L0 78 Z" fill="var(--green)"/>
    <path d="M0 69 C110 59 225 79 350 63 L350 78 L0 78 Z" fill="var(--blue)"/>
  </svg>
</div>
<div class="caption" style="left:826px;top:408px;width:350px;">Envelope Front &amp; Back</div>

</body>
</html>
```